Zielgruppe
Beamer Vermietung
Aufgabenstellung
Erstellung 2 professionell aussehender Webseiten.
Projektor-Verleih-Region-Wendlar.de
sowie
Projektor-Verleih-Region-Haselfurtheim.de
Die Seiten sind aktuell im Betrieb, aber haben ein sehr veraltetes Design.
Die Seiten können ähnlich aussehen, sollten aber etwas unterschiedlich sein, damit sie für den Kunden leicht anders aussehen.
Wichtig ist, dass alle Seiten, inklusive Startseite, Unterseiten und Links designed werden und das dieses Design in die bestehende Seitenwerk Installation eingepflegt wird.
Es ist also notwendig, gute Seitenwerk Kenntnisse zu haben um dann auch zwei fertige Seitenwerk Seiten liefern zu können.

```html
<!DOCTYPE html>
<html lang="de">
<head>
<meta charset="utf-8">
<title>Preisliste – Beamer und Leinwand Vermietung</title>
<link rel="stylesheet" href="https://fonts.googleapis.com/css2?family=Roboto:ital,wght@0,300;0,400;0,500;0,700;1,700&family=Roboto+Condensed:wght@400&display=swap">
<style>
:root{
  --navy:#1e3d66;
  --navy-dark:#162a47;
  --yellow:#f5c518;
  --topbar:#ececec;
  --row-alt:#efefef;
  --text:#555b63;
  --white:#ffffff;
}
*{margin:0;padding:0;box-sizing:border-box}
html,body{width:767px;height:1200px;overflow:hidden;background:var(--white);font-family:"Roboto",Arial,sans-serif}
.page{position:relative;width:767px;height:1200px}

.topbar{height:20px;background:var(--topbar);border-bottom:1px solid #dcdcdc;display:flex;align-items:center;justify-content:space-between;padding:0 104px 0 104px}
.topbar__url{font-size:6.8px;color:#666;font-weight:300}
.topbar__social{display:flex;gap:8px;margin-right:7px}
.topbar__social span{width:11px;height:11px;border-radius:50%;background:var(--navy)}
.topbar__social span:first-child{background:var(--yellow)}

.header{height:46px;display:flex;align-items:center;justify-content:space-between;padding:0 103px 0 102px}
.header__title{font-family:"Roboto Condensed",Arial,sans-serif;font-size:21px;color:var(--navy);letter-spacing:-.1px}
.header__links{display:flex;align-items:center;gap:12px;font-size:8.6px;color:var(--navy);font-weight:500;padding-top:2px}
.header__links a{color:inherit;text-decoration:none;display:flex;align-items:center;gap:6px}

.nav{height:31px;background:var(--navy);display:flex;justify-content:flex-end;padding-right:100px}
.nav a{color:var(--white);font-size:9.2px;font-weight:500;text-decoration:none;display:flex;align-items:center;padding:0 6.4px;letter-spacing:.1px}
.nav a.is-active{background:var(--yellow)}

.hero{position:relative;height:106px;background:linear-gradient(180deg,#6784a5 0%,#8ea9c3 100%);overflow:hidden}
.hero__photo{position:absolute;left:425px;top:0;width:342px;height:106px;background:linear-gradient(90deg,rgba(160,180,200,0) 0%,rgba(170,188,206,.55) 45%,rgba(150,170,192,.35) 100%)}
.hero__bar{position:absolute;left:104px;top:33px;width:18px;height:2px;background:var(--yellow)}
.hero__title{position:absolute;left:103px;top:36px;font-size:30px;font-weight:700;color:var(--white)}

.prices{position:absolute;left:176px;top:241px;width:416px;box-shadow:0 0 5px rgba(0,0,0,.12);background:var(--white)}
.price-item{display:flex;flex-direction:column;justify-content:center;padding:0 17px 0 24px}
.price-item:nth-child(even){background:var(--row-alt)}
.price-item__name{font-size:12px;font-weight:500;color:var(--navy);letter-spacing:.2px;margin-bottom:3px}
.price-item__line{display:flex;font-size:10.4px;color:var(--text);line-height:17.5px;padding-left:1px}
.price-item__line span:first-child{width:265px}
.price-item--tall{height:72px}
.price-item--short{height:71px}
.prices__note{height:47px;display:flex;align-items:center;padding-left:30px;font-size:10.2px;font-weight:700;font-style:italic;color:#333}

.booking{position:absolute;left:0;top:1047px;width:767px;height:105px;background:var(--navy);text-align:center}
.booking__title{font-size:26.5px;font-weight:700;color:var(--yellow);margin-top:18px}
.booking__phones{display:flex;justify-content:center;gap:86px;margin-top:4px}
.booking__phone{display:flex;align-items:center;gap:12px;color:var(--white);font-size:20.5px;font-weight:300;letter-spacing:.3px}

.footer{position:absolute;left:0;top:1152px;width:767px;height:48px;background:var(--navy-dark);color:#e4e8ee;font-size:7px;text-align:center;padding-top:14px;line-height:14.5px;font-weight:300}
</style>
</head>
<body>
<div class="page">
  <div class="topbar">
    <span class="topbar__url">www.projektor-verleih-region-haselfurtheim.de</span>
    <div class="topbar__social"><span></span><span></span><span></span><span></span></div>
  </div>

  <header class="header">
    <div class="header__title">Beamer und Leinwand Vermietung</div>
    <div class="header__links">
      <a href="#"><svg width="12" height="9" viewBox="0 0 12 9"><rect x=".5" y=".5" width="11" height="8" fill="none" stroke="#1e3d66"/><path d="M.5 .5 6 5 11.5 .5M.5 8.5 4.5 4.5M11.5 8.5 7.5 4.5" fill="none" stroke="#1e3d66"/></svg>Kontakt / Anreise</a>
      <a href="#">Impressum</a>
    </div>
  </header>

  <nav class="nav">
    <a href="#">Beamer mieten</a>
    <a href="#">HD Beamer mieten</a>
    <a href="#">Full-HD Beamer mieten</a>
    <a href="#">Reservieren oder Buchen</a>
    <a href="#" class="is-active">Preisliste</a>
    <a href="#">Datenschutzerklärung</a>
  </nav>

  <section class="hero">
    <div class="hero__photo" role="img" aria-label="Foto einer Hand mit Stift über einer Zahlentabelle"></div>
    <div class="hero__bar"></div>
    <h1 class="hero__title">Preisliste</h1>
  </section>

  <section class="prices">
    <div class="price-item price-item--tall">
      <div class="price-item__name">Beamer Modell Lumora LX 300</div>
      <div class="price-item__line"><span>pro Werktag</span><span>€ 30,00</span></div>
      <div class="price-item__line"><span>pro Wochenende (Fr.-So. / Sa.-Mo.)</span><span>€ 45,00</span></div>
    </div>
    <div class="price-item price-item--tall">
      <div class="price-item__name">HD-Beamer Modell Viscora V210</div>
      <div class="price-item__line"><span>pro Werktag</span><span>€ 40,00</span></div>
      <div class="price-item__line"><span>pro Wochenende (Fr.-So. / Sa.-Mo.)</span><span>€ 60,00</span></div>
    </div>
    <div class="price-item price-item--tall">
      <div class="price-item__name">Full-HD-Beamer Modell Brightel FX 40</div>
      <div class="price-item__line"><span>pro Werktag</span><span>€ 70,00</span></div>
      <div class="price-item__line"><span>pro Wochenende (Fr.-So. / Sa.-Mo.)</span><span>€ 120,00</span></div>
    </div>
    <div class="price-item price-item--tall">
      <div class="price-item__name">Leinwand (optional zubuchbar)</div>
      <div class="price-item__line"><span>pro Werktag</span><span>€ 15,00</span></div>
      <div class="price-item__line"><span>pro Wochenende (Fr.-So. / Sa.-Mo.)</span><span>€ 25,00</span></div>
    </div>
    <div class="price-item price-item--short">
      <div class="price-item__name">SAT Verlängerungskabel 10 Meter (optional zubuchbar)</div>
      <div class="price-item__line"><span>pro Ausleihung</span><span>€ 5,00</span></div>
    </div>
    <div class="price-item price-item--short">
      <div class="price-item__name">HDMI Verlängerungskabel 10 Meter (optional zubuchbar)</div>
      <div class="price-item__line"><span>pro Ausleihung</span><span>€ 5,00</span></div>
    </div>
    <div class="price-item price-item--short">
      <div class="price-item__name">Strom Verlängerungskabel 10 bis 25 Meter (optional zubuchbar)</div>
      <div class="price-item__line"><span>pro Ausleihung</span><span>€ 5,00</span></div>
    </div>
    <div class="price-item price-item--short">
      <div class="price-item__name">Anreisekosten für Bring-Service (optional zubuchbar)</div>
      <div class="price-item__line"><span>pro gefahrenem km</span><span>€ 0,35</span></div>
    </div>
    <div class="price-item price-item--short">
      <div class="price-item__name">zusätzlicher Aufbau-Service (optional zubuchbar)</div>
      <div class="price-item__line"><span>pro Ausleihung</span><span>€ 20,00</span></div>
    </div>
    <div class="price-item price-item--short">
      <div class="price-item__name">zusätzlicher Abbau-Service (optional zubuchbar)</div>
      <div class="price-item__line"><span>pro Ausleihung</span><span>€ 10,00</span></div>
    </div>
    <div class="prices__note">Alle Preise beinhalten 19% gesetzliche Mehrwertsteuer.</div>
  </section>

  <section class="booking">
    <h2 class="booking__title">Reservieren oder Buchen</h2>
    <div class="booking__phones">
      <div class="booking__phone">
        <svg width="22" height="16" viewBox="0 0 22 16"><path d="M1 5C1 1 21 1 21 5v2h-5V4.5H6V7H1z" fill="#f5c518"/><path d="M5 8h12l3 7H2z" fill="#f5c518"/><circle cx="11" cy="11" r="2.3" fill="#1e3d66"/></svg>
        02741/555210
      </div>
      <div class="booking__phone">
        <svg width="24" height="27" viewBox="0 0 24 27"><rect x="1" y="2" width="15" height="24" rx="2" fill="none" stroke="#f5c518" stroke-width="1.4"/><line x1="1" y1="21" x2="16" y2="21" stroke="#f5c518" stroke-width="1.2"/><path d="M5 9c1-1 2 1 2 2s-1 1 0 2 1 2 2 1 3 1 2 2-4 0-5-2-2-4-1-5z" fill="none" stroke="#f5c518" stroke-width="1"/><path d="M19 3c2 1 2 4 0 5M21 1c3 2 3 7 0 9" fill="none" stroke="#f5c518" stroke-width="1"/></svg>
        0151/5550437
      </div>
    </div>
  </section>

  <footer class="footer">
    Copyright © 2020 Projektor-Verleih-Region-Haselfurtheim.de – Beamer mieten in Haselfurtheim. Alle Rechte vorbehalten.<br>
    Theme: Blattwerk von Vorlagenhaus. Bereitgestellt von Seitenwerk.
  </footer>
</div>
</body>
</html>
```